Meridian Cataract Surgery and Cosmetic Eyelid Surgery

We need Three page website design (home page and interior page template with two looks) with accompanying CSS code. 1. Home page, 2. General Eye-Care page, 3. Cosmetic Eyelid Surgery. #2 an #3 would be only slightly different. See below.

The site being redesigned is http://www.bright-lumen.com.

The content will remain consistent with the current site.

Additional graphics will be included, especially a number of "Before and after" photos of patients for the various procedures.

You can see competitive sites here: http://www.findoraq.com/search?q=cosmetic+eyelid+surgury+santa+rosa&ie=utf-8&oe=utf-8&aq=t&client=browser-b&rlz=1R1TTPP_en___US384

The client likes http://www.view-pmr.com, which has a serious look he likes (not necessarily the colors or design). Avoid too many "happy loving couples" and pretty women, on the main page or cataract/general eye-care pages. They are, however, good on the cosmetic pages.

When patients look at the *cosmetic surgery* pages, they can see the pretty women/couples. For *eye surgery* (which is what this is all about) they should see an attractive, active OLDER couple(s) on cataract surgery and refractive surgery pages.

In the US, premium IOL (Intraocular lens - a clear plastic lens that is implanted in the eye; usually done when the natural lens has been removed in a cataract operation) cataract surgery, cosmetic and refractive surgery are not fully paid for by insurance, so patients can afford to pay for it themselves and are more well-off than the normal market.
Updates

Do not use the graphics or look and feel of the current site.  We are looking for a NEW design, not a remix of the old elements.

The new logo is at http://www.artmarketo.com/file.aspx?fileLocation=claritonvisionlogo0.jpg

 
Do NOT use the old logo.  If your submitted design uses the old logo, please fix it and delete the one with the old logo.

Sorry for not making this clearer when we started.

Normal 0 false false false EN-US X-NONE X-NONE I want to see a home page that gives equal billing to general eyecare and cosmetic and RECONSTRUCTIVE eyelid surgery.   General eyecare should be listed first.  This should have the correct Practice name and Logo:   Meridian Sightcare and Cosmetic Eyelid Surgery Center.  The home page should be inviting to both old and young, men and women.  The General eyecare page should have similar appeal.  Cosmetic Page should be decidedly more feminine.  The home page should also highlight Dr. Brennick' s qualification and provide a site map/navigation.

The colors of the logo do not need to be limited to black and white.  The logos MUST be integrated into the design, not just pasted on the page.

Read the brief carefully and pay careful attention to the target markets.

 

vector art uploaded:  logo.ai

Target Market(s)

OLDER men and women. People whose faces, eyes, etc., have an aged look that they want to look younger. ALSO patients who want to have the best possible vision after CATARACT SURGERY. Patients who want Premium IOL'S which give them vision at both distance and near WITHOUT GLASSES. STATE OF THE ART GLAUCOMA SURGERY.

Industry/Entity Type

Plastic

Requirements
Must have
• Easy to read. Some readers may have vision difficulties. Easy to navigate for the elderly market. Cosmetic page may be a little more complex.

```html
<!DOCTYPE html>
<html lang="en">
<head>
<meta charset="utf-8">
<title>Meridian Sightcare and Cosmetic Eyelid Surgery Center</title>
<link href="https://fonts.googleapis.com/css2?family=Open+Sans:wght@300;400;600;700&display=swap" rel="stylesheet">
<style>
:root{
  --navy:#1d3f7a;
  --navy-dark:#132c5a;
  --cyan:#2bb3e4;
  --cyan-light:#c9ecf8;
  --sky:#5fb8e6;
  --ink:#3b3b3b;
  --muted:#777;
  --line:#d9e3ea;
  --paper:#ffffff;
  --mist:#f2f6f9;
}
*{box-sizing:border-box;margin:0;padding:0}
html,body{width:880px;height:1200px;overflow:hidden;background:var(--paper)}
body{font-family:"Open Sans",Arial,sans-serif;color:var(--ink);font-size:11px;line-height:1.45}
.page{width:880px;height:1200px;position:relative}
.masthead{height:66px;display:flex;align-items:center;padding:0 28px;justify-content:space-between}
.brand{display:flex;align-items:center;gap:8px;font-size:20px;font-weight:700;color:var(--navy)}
.brand-dot{width:16px;height:16px;border-radius:50%;background:var(--cyan)}
.tagline{font-size:11px;color:var(--muted);flex:1;margin-left:22px}
.address{font-size:9px;color:var(--muted);text-align:right;line-height:1.35}
.nav{height:26px;background:var(--navy);display:flex;padding:0 28px}
.nav a{color:#fff;text-decoration:none;font-size:10px;font-weight:600;padding:0 16px;line-height:26px;border-right:1px solid rgba(255,255,255,.25)}
.nav a.active{background:var(--cyan)}
.hero{height:238px;position:relative;display:flex;overflow:hidden}
.hero-copy{width:290px;background:linear-gradient(135deg,#3f9fd8,#9fd8f3);color:#fff;padding:50px 26px}
.hero-copy h1{font-weight:300;font-size:24px;line-height:1.25;margin-bottom:22px}
.hero-copy p{font-size:14px}
.hero-photo{width:250px;background:linear-gradient(160deg,#e8d4c6,#cfb3a2 60%,#a98c7c)}
.hero-links{flex:1;position:relative;background:#eef8fc}
.hero-links svg{position:absolute;inset:0}
.hero-link{position:absolute;color:var(--cyan);font-size:16px;font-weight:400;line-height:1.2}
.content{padding:0 28px}
.welcome h2{font-weight:300;font-size:38px;color:var(--sky);margin:10px 0 4px}
.welcome p{font-size:10.5px;margin-bottom:8px}
.panel{border:1px solid var(--line);background:var(--mist)}
.panel-head{background:linear-gradient(90deg,var(--cyan),#6dd0ef);color:#fff;font-size:13px;font-weight:600;padding:7px 12px}
.panel-body{padding:10px 14px;font-size:10px}
.panel-body li{list-style:none;margin-bottom:4px}
.panel-body b{color:var(--navy)}
.cols{display:flex;gap:16px;margin-top:14px}
.eyecare{width:380px}
.eyecare ul{margin-top:8px}
.eyecare li::before{content:"▸ ";color:var(--cyan)}
.gallery{flex:1;border:1px solid var(--line);padding:10px 12px}
.gallery h3{font-size:12px;font-weight:600;text-align:center;margin-bottom:10px}
.ba{display:flex;gap:10px}
.ba-item{flex:1;text-align:center;font-size:10px}
.ba-item span{display:block;color:var(--cyan);font-weight:600;margin-bottom:4px}
.ba-photo{height:120px;background:linear-gradient(180deg,#d9bfae,#b89686)}
.ba-item p{font-size:9px;color:var(--muted);margin-top:4px}
.more{text-align:right;font-size:11px;color:var(--navy);margin-top:10px}
.cta{text-align:center;font-size:10px;margin:14px 0;color:var(--muted)}
.cta a{color:var(--cyan)}
.lower{display:flex;gap:30px;border-top:1px solid var(--line);padding-top:14px;height:210px}
.lower h4{font-size:12px;color:var(--navy);font-weight:600;margin-bottom:8px}
.lower .col{flex:1;font-size:10px}
.lower ul{list-style:none}
.lower li{margin-bottom:3px}
.footer{position:absolute;left:0;right:0;bottom:0;height:34px;background:var(--navy);display:flex;justify-content:center;align-items:center;gap:30px}
.footer a{color:#fff;font-size:10px;text-decoration:none}
</style>
</head>
<body>
<div class="page">
  <header class="masthead">
    <div class="brand"><span class="brand-dot"></span>Meridian Sightcare</div>
    <div class="tagline">Meridian Sightcare and Cosmetic Eyelid Surgery Center</div>
    <div class="address">Robert A. Brennick M.D.<br>412 Larkfield Avenue<br>Alder Creek, CA<br>(555) 014-EYES</div>
  </header>
  <nav class="nav">
    <a class="active" href="#">About Cosmetic Eyelid Surgery</a>
    <a href="#">Patient Photos</a>
    <a href="#">About Dr. Robert Brennick</a>
    <a href="#">Map to Our Office</a>
    <a href="#">Contact Us</a>
  </nav>
  <section class="hero">
    <div class="hero-copy">
      <h1>Enhancing the beauty of your face!</h1>
      <p>Eyelid and Facial Cosmetic Surgery</p>
    </div>
    <div class="hero-photo" role="img" aria-label="Close-up portrait photograph of a woman's face and eyes"></div>
    <div class="hero-links">
      <svg width="340" height="238" viewBox="0 0 340 238">
        <polygon points="0,0 340,0 340,80 20,80" fill="#ffffff"/>
        <polygon points="20,86 340,86 340,160 40,160" fill="#ffffff"/>
        <polygon points="40,166 340,166 340,238 60,238" fill="#ffffff"/>
      </svg>
      <div class="hero-link" style="left:50px;top:20px">Cosmetic Eyelid Surgery<br>For Men and Women</div>
      <div class="hero-link" style="left:70px;top:104px">How Aesthetic Eyelid<br>Surgery is Performed</div>
      <div class="hero-link" style="left:90px;top:192px">General Eye Care</div>
    </div>
  </section>
  <main class="content">
    <section class="welcome">
      <h2>welcome</h2>
      <p>Dr. Brennick specializes in cosmetic and reconstructive surgery of the eyelids and upper face. Because he performs these procedures with refined, gentle technique, his patients enjoy less bruising and swelling and are back to work and daily life sooner than they expect.</p>
      <p>Dr. Brennick is one of only a few eyelid surgeons nationally who are trained in both the reconstruction and beautification of eyelids, following his residency in Ophthalmology. He has completed a formal fellowship in eyelid plastic and orbital surgery. Find out if cosmetic eyelid or facial plastic surgery is right for you, and learn more about how these procedures are performed.</p>
    </section>
    <section class="panel">
      <div class="panel-head">How Aesthetic Eyelid Surgery is Performed</div>
      <ul class="panel-body">
        <li><b>Upper Eyelift:</b> Advanced laser eyelift surgery removes excess skin and lifts heavy upper lids with minimal scarring.</li>
        <li><b>Lower Eyelift:</b> Bags under the eyes can often be removed without visible incisions.</li>
        <li><b>Forehead/Brow:</b> Endoscopic brow lift improves brow and forehead position and contour with small incisions.</li>
        <li><b>Laser Skin Resurfacing:</b> Smooths fine lines and wrinkles around the eyes for a fresh look.</li>
      </ul>
    </section>
    <div class="cols">
      <section class="panel eyecare">
        <div class="panel-head">General Eye Care</div>
        <div class="panel-body">
          <p>Robert A. Brennick, MD is certified by the American Board of Ophthalmology and is a member of the American College of Eye Surgeons. He is an expert in the management of cataracts, glaucoma, diabetic retinopathy, dry eye problems and macular disease. Please click on the links below for more information about diseases of the eye and their treatments.</p>
          <ul>
            <li>Cataracts</li>
            <li>Diabetic Retinopathy</li>
            <li>Floaters and Flashes</li>
            <li>Glaucoma</li>
            <li>Macular Degeneration</li>
          </ul>
        </div>
      </section>
      <section class="gallery">
        <h3>4 Upper Eyelid Blepharoplasty and Ptosis Repair</h3>
        <div class="ba">
          <div class="ba-item"><span>Before</span><div class="ba-photo" role="img" aria-label="Before photograph of a patient's eye area"></div><p>Heavy lids covering the upper eye</p></div>
          <div class="ba-item"><span>After</span><div class="ba-photo" role="img" aria-label="After photograph of a patient's eye area"></div><p>Brighter, more open eyes after repair</p></div>
        </div>
        <div class="more">See more photos ›</div>
      </section>
    </div>
    <p class="cta">If you would like to find out more about the office and scheduling appointments, <a href="#">click here</a></p>
    <section class="lower">
      <div class="col">
        <h4>General Ophthalmology</h4>
        <ul>
          <li>Cataracts</li>
          <li>Diabetic Retinopathy</li>
          <li>Floaters and Flashes</li>
          <li>Glaucoma</li>
          <li>Macular Degeneration</li>
          <li>Refractive Surgery</li>
        </ul>
      </div>
      <div class="col">
        <h4>Our mission</h4>
        <p>Is to provide personal, friendly, state of the art general eye care as well as the latest advances in cosmetic eyelid surgery for men and women.</p>
        <p style="margin-top:10px">Robert A. Brennick M.D., 412 Larkfield Avenue, Alder Creek, CA (555) 014-EYES</p>
      </div>
    </section>
  </main>
  <footer class="footer">
    <a href="#">About Cosmetic Eyelid Surgery</a>
    <a href="#">Patient Photos</a>
    <a href="#">About Dr. Robert Brennick</a>
    <a href="#">Map to Our Office</a>
    <a href="#">Contact Us</a>
  </footer>
</div>
</body>
</html>
```